WWW.VELTRONA.IT BUSINNES CARD

WE NEED A BUSINESS CARD . I HAVE A COMPANY IN ITALY NR 1 IN HAIR MEDICAL CARE AN HAIR REPLECEMENT . IN CARD I NEED WRITE WEB ADDRESS, MAIL , ADDRESS, TELEPHONE NUMBER , AND NAME
IN THE BACK SIDE I NEED MY DOCTOR LOGO .
MY WEB SITE IS WWW.VELTRONA.IT
Updates

Target Market(s)

CONSUMER B2C

Industry/Entity Type

Hair And Beauty

Contact Information for Business Card

I WANT A MEDICAL BUSINESS CARD.

Font styles to use
Other font styles liked:
• VERDANA

Colors
33a6d7
3176b5
85abd2
aedbee
eaf1f7
ffffff

Requirements
Must have
• I NEED MY LOGO AND LOGO OF DR VELTRONA

```html
<!DOCTYPE html>
<html lang="it">
<head>
<meta charset="utf-8">
<title>Veltrona – Business Card</title>
<link href="https://fonts.googleapis.com/css2?family=Open+Sans:ital,wght@0,300;0,400;0,600;0,700;1,600;1,700&display=swap" rel="stylesheet">
<style>
  :root{
    --blue-bright:#33a6d7;
    --blue-deep:#3176b5;
    --blue-mid:#85abd2;
    --blue-light:#aedbee;
    --blue-pale:#eaf1f7;
    --white:#ffffff;
    --sheet:#eef0f2;
    --shade:#d5d8db;
    --shade-dark:#c4c8cc;
    --grey-text:#8a8f94;
  }
  *{margin:0;padding:0;box-sizing:border-box}
  html,body{width:796px;height:1200px;overflow:hidden}
  body{position:relative;background:var(--sheet);font-family:"Open Sans",Verdana,sans-serif;color:var(--blue-deep)}
  .backdrop{position:absolute;inset:0}
  .sheet-title{position:absolute;left:58px;top:26px;color:var(--grey-text);letter-spacing:2px}
  .sheet-title .line-1{font-size:28px;font-weight:300;line-height:34px}
  .sheet-title .line-1 b{font-weight:700}
  .sheet-title .line-2{font-size:17px;font-weight:300}
  .sheet-title .line-2 b{font-weight:700}
  .sheet-notes{position:absolute;right:58px;top:30px;text-align:right;color:var(--grey-text);font-size:12px;letter-spacing:1.5px;line-height:18px}
  .sheet-notes .strong{font-weight:700;color:#6f757a}

  .card{position:absolute;left:58px;width:680px;background:linear-gradient(160deg,var(--white) 0%,var(--blue-pale) 55%,#dcebf6 100%);box-shadow:0 4px 14px rgba(0,0,0,.12)}
  .card-frame{position:absolute;inset:22px;border:2px solid var(--blue-bright)}
  .card--front{top:138px;height:480px}
  .card--back{top:685px;height:335px}

  .brand{position:absolute;left:0;right:0;text-align:center}
  .brand-name{display:inline-flex;align-items:center;gap:14px;font-size:58px;font-weight:700;color:var(--blue-deep);line-height:1}
  .brand-dot{width:34px;height:34px;border-radius:50%;background:var(--blue-bright)}
  .brand-tagline{font-size:17px;font-weight:600;color:var(--blue-deep);letter-spacing:1px;margin-top:6px}
  .card--front .brand{top:82px}

  .doctor-name{font-style:italic;font-weight:700;color:var(--blue-bright)}
  .card--front .doctor-name{position:absolute;left:0;right:0;top:246px;text-align:center;font-size:34px}
  .address{position:absolute;left:0;right:0;top:314px;display:flex;justify-content:center;align-items:center;gap:12px;font-size:19px;color:var(--blue-deep)}
  .contact-bar{position:absolute;left:190px;right:60px;top:365px;height:50px;border-top:2px solid var(--blue-bright);border-bottom:2px solid var(--blue-bright);display:flex;justify-content:space-around;align-items:center;font-size:18px;color:var(--blue-deep)}
  .contact-item{display:flex;align-items:center;gap:10px}

  .question{position:absolute;left:90px;top:86px;color:var(--blue-bright);font-size:26px;line-height:34px}
  .question .ask{font-size:26px}
  .question .doctor-name{font-size:38px;display:block;margin-top:14px}
  .bubble{position:absolute;left:296px;top:40px}
  .mascot{position:absolute;left:430px;top:30px;width:170px;height:270px;border-radius:80px 80px 40px 40px;background:linear-gradient(180deg,#6b3f24 0%,#8a5a36 55%,var(--blue-mid) 100%);opacity:.85}
  .website{position:absolute;left:90px;top:238px;display:flex;align-items:center;gap:12px;font-size:22px;font-weight:700;color:var(--blue-deep)}

  .footer-brand{position:absolute;left:0;right:0;top:1085px;text-align:center}
  .footer-brand .brand-name{font-size:48px}
  .footer-brand .brand-dot{width:28px;height:28px}
  .footer-brand .brand-tagline{font-size:14px}
</style>
</head>
<body>
  <svg class="backdrop" width="796" height="1200" viewBox="0 0 796 1200" aria-hidden="true">
    <polygon points="0,520 160,640 0,900" fill="var(--shade-dark)"/>
    <polygon points="0,900 796,620 796,860 0,1200" fill="var(--shade)"/>
  </svg>

  <header class="sheet-title">
    <div class="line-1">CLEAN <b>MORDEN</b></div>
    <div class="line-2"><b>TEXTURE</b> BACKGROUND</div>
  </header>
  <div class="sheet-notes">
    <div class="strong">BUSINESS CARD DESIGN</div>
    <div>PRINT READY</div>
    <div>FULL EDITABLE</div>
  </div>

  <section class="card card--front">
    <div class="card-frame"></div>
    <div class="brand">
      <div class="brand-name"><span class="brand-dot"></span>Veltrona</div>
      <div class="brand-tagline">CURA E REINTEGRAZIONE DEI CAPELLI</div>
    </div>
    <div class="doctor-name">Dr. Veltrona</div>
    <div class="address">
      <svg width="24" height="22" viewBox="0 0 24 22"><path d="M12 1 1 11h3v10h6v-6h4v6h6V11h3z" fill="var(--blue-deep)"/></svg>
      <span>Via Lunga 14, Treviso, Italy</span>
    </div>
    <div class="contact-bar">
      <span class="contact-item">
        <svg width="22" height="16" viewBox="0 0 22 16"><rect x="1" y="1" width="20" height="14" rx="2" fill="var(--blue-bright)"/><path d="M1 2l10 7 10-7" fill="none" stroke="var(--white)" stroke-width="1.6"/></svg>
        info@veltrona.it
      </span>
      <span class="contact-item">
        <svg width="20" height="20" viewBox="0 0 20 20"><rect width="20" height="20" rx="3" fill="var(--blue-bright)"/><path d="M6 4c1 0 2 2 2 3s-1 1-1 2 2 3 3 3 1-1 2-1 3 1 3 2-1 2-2 2C9 15 5 11 5 6c0-1 0-2 1-2z" fill="var(--white)"/></svg>
        +39041287760
      </span>
    </div>
  </section>

  <section class="card card--back">
    <div class="card-frame"></div>
    <div class="question">
      <div class="ask">Hai una domanda?</div>
      <div class="ask">Chiedi consiglio a</div>
      <span class="doctor-name">Dr. Veltrona</span>
    </div>
    <svg class="bubble" width="50" height="56" viewBox="0 0 50 56" aria-hidden="true">
      <circle cx="25" cy="25" r="22" fill="var(--white)" stroke="var(--blue-bright)" stroke-width="3"/>
      <path d="M14 44 8 54 24 47z" fill="var(--blue-bright)"/>
      <text x="25" y="34" text-anchor="middle" font-family="Open Sans, sans-serif" font-weight="700" font-size="26" fill="var(--blue-bright)">?</text>
    </svg>
    <div class="mascot" role="img" aria-label="Cartoon mascot: a tall strand of hair dressed as a doctor with a white coat, giving a thumbs up"></div>
    <div class="website">
      <svg width="24" height="24" viewBox="0 0 24 24"><circle cx="12" cy="12" r="11" fill="var(--blue-bright)"/><path d="M1 12h22M12 1c-5 5-5 17 0 22M12 1c5 5 5 17 0 22" fill="none" stroke="var(--white)" stroke-width="1.4"/></svg>
      <span>www.veltrona.it</span>
    </div>
  </section>

  <footer class="footer-brand">
    <div class="brand-name"><span class="brand-dot"></span>Veltrona</div>
    <div class="brand-tagline">CURA E REINTEGRAZIONE DEI CAPELLI</div>
  </footer>
</body>
</html>
```